Aggressive Appliance retailer requires a Large Billboard design.

We require a large Tall billboard design it stands 4500mm high x 2400mm across. We have our own range of imported appliances called Velocane and we provide a 5 year warranty, key pionts low price + long solid warranty. Provided are 3 products 1 x clothes washer 8 kg $699 1 x dishwasher $499 1 x side by side fridge freezer $1299 all with 5 year warranty. Company colors very bright green. Provided warranty logo / images / and an add that has the font we have preference too. I am not rigid to the above requirements and open to designers own ideas :-) I have supplied a few dishwasher images if you want one with closed door i may need to sort one out

```html
<!DOCTYPE html>
<html lang="en">
<head>
<meta charset="utf-8">
<title>Velocane Appliances – Billboard</title>
<link href="https://fonts.googleapis.com/css2?family=Anton&family=Bebas+Neue&display=swap" rel="stylesheet">
<style>
  :root {
    --lime: #8dc63f;
    --lime-light: #c9df3b;
    --lime-pale: #a6d13f;
    --green-deep: #4fa13a;
    --brand-green: #0c9a47;
    --red: #e04a32;
    --black: #0d0d0d;
    --white: #ffffff;
    --yellow: #fff200;
    --steel: #c9cbcc;
    --appliance-white: #e9eaeb;
  }
  html, body {
    margin: 0;
    padding: 0;
    width: 1200px;
    height: 2251px;
    overflow: hidden;
    background: var(--lime);
  }
  .billboard {
    display: block;
    width: 1200px;
    height: 2251px;
  }
  .brand-name {
    font-family: "Anton", sans-serif;
    fill: var(--black);
  }
  .price-text, .label-text, .warranty-text {
    font-family: "Bebas Neue", sans-serif;
  }
  .price-text { fill: var(--white); }
  .label-text { fill: var(--white); }
  .warranty-text { fill: var(--black); }
</style>
</head>
<body>
<svg class="billboard" viewBox="0 0 500 938" preserveAspectRatio="none" xmlns="http://www.w3.org/2000/svg">
  <defs>
    <linearGradient id="steel-tone" x1="0" y1="0" x2="1" y2="0">
      <stop offset="0" stop-color="#b9bcbe"/>
      <stop offset="0.5" stop-color="#dcdedf"/>
      <stop offset="1" stop-color="#b4b7b9"/>
    </linearGradient>
    <linearGradient id="white-tone" x1="0" y1="0" x2="1" y2="1">
      <stop offset="0" stop-color="#f4f5f6"/>
      <stop offset="1" stop-color="#cfd2d4"/>
    </linearGradient>
  </defs>

  <!-- background blocks -->
  <g class="backdrop">
    <rect width="500" height="938" fill="var(--lime)"/>
    <rect x="0" y="0" width="85" height="110" fill="var(--lime-light)"/>
    <rect x="170" y="0" width="90" height="110" fill="var(--lime-pale)"/>
    <rect x="330" y="0" width="170" height="40" fill="var(--lime-light)"/>
    <rect x="85" y="110" width="85" height="100" fill="var(--lime-light)"/>
    <rect x="260" y="110" width="90" height="100" fill="var(--green-deep)"/>
    <rect x="0" y="210" width="85" height="110" fill="var(--green-deep)"/>
    <rect x="170" y="210" width="90" height="110" fill="var(--lime-light)"/>
    <rect x="430" y="210" width="70" height="110" fill="var(--lime-light)"/>
    <rect x="260" y="320" width="90" height="110" fill="var(--lime-light)"/>
    <rect x="430" y="430" width="70" height="110" fill="var(--green-deep)"/>
    <rect x="0" y="430" width="85" height="110" fill="var(--lime-light)"/>
    <rect x="260" y="540" width="90" height="110" fill="var(--green-deep)"/>
    <rect x="430" y="640" width="70" height="110" fill="var(--lime-light)"/>
    <rect x="170" y="760" width="90" height="120" fill="var(--lime-light)"/>
  </g>

  <!-- rings behind products -->
  <g class="product-rings">
    <circle cx="405" cy="330" r="128" fill="var(--red)"/>
    <circle cx="405" cy="330" r="116" fill="var(--black)"/>
    <circle cx="140" cy="555" r="200" fill="var(--brand-green)"/>
    <circle cx="140" cy="555" r="188" fill="var(--red)"/>
    <circle cx="140" cy="555" r="176" fill="var(--black)"/>
    <circle cx="345" cy="770" r="180" fill="var(--red)"/>
    <circle cx="345" cy="770" r="168" fill="var(--black)"/>
  </g>

  <!-- bottom band -->
  <path class="bottom-band" d="M180 938 L500 860 L500 938 Z" fill="var(--red)"/>

  <!-- brand name -->
  <g class="brand">
    <text class="brand-name" x="38" y="100" font-size="66" letter-spacing="-1">Velocane</text>
    <text class="brand-name" x="40" y="136" font-size="24" letter-spacing="5">APPLIANCES</text>
  </g>

  <!-- header stripes -->
  <g class="header-stripes">
    <rect x="280" y="42" width="220" height="16" fill="var(--red)"/>
    <rect x="308" y="68" width="192" height="14" fill="var(--white)"/>
    <rect x="340" y="94" width="160" height="14" fill="var(--white)"/>
    <rect x="278" y="118" width="222" height="14" fill="var(--brand-green)"/>
  </g>

  <!-- product photos -->
  <g class="product-photo fridge-photo" role="img" aria-label="Stainless steel side by side fridge freezer">
    <rect x="8" y="280" width="220" height="382" rx="4" fill="url(#steel-tone)"/>
  </g>
  <g class="product-photo washer-photo" role="img" aria-label="White top loading 8 kg clothes washer">
    <path d="M278 235 L460 210 L470 440 L292 462 Z" fill="url(#white-tone)"/>
  </g>
  <g class="product-photo dishwasher-photo" role="img" aria-label="White freestanding dishwasher">
    <rect x="232" y="606" width="224" height="300" rx="3" fill="url(#white-tone)"/>
  </g>

  <!-- price tags -->
  <g class="price-tag price-fridge" transform="rotate(7 115 222)">
    <path d="M30 175 H200 V268 H170 L182 296 L140 268 H30 Z" fill="var(--red)" stroke="var(--white)" stroke-width="4" stroke-linejoin="round"/>
    <text class="price-text" x="115" y="250" font-size="66" text-anchor="middle">$1299</text>
  </g>
  <g class="price-tag price-washer" transform="rotate(-10 405 190)">
    <path d="M345 152 H465 V224 H400 L370 250 L378 224 H345 Z" fill="var(--red)" stroke="var(--white)" stroke-width="4" stroke-linejoin="round"/>
    <text class="price-text" x="405" y="212" font-size="56" text-anchor="middle">$699</text>
  </g>
  <g class="price-tag price-dishwasher" transform="rotate(-12 390 565)">
    <path d="M318 520 H462 V605 H390 L352 632 L362 605 H318 Z" fill="var(--red)" stroke="var(--white)" stroke-width="4" stroke-linejoin="round"/>
    <text class="price-text" x="390" y="590" font-size="68" text-anchor="middle">$499</text>
  </g>

  <!-- product labels -->
  <g class="product-label label-washer">
    <rect x="266" y="413" width="222" height="50" fill="var(--green-deep)" stroke="var(--white)" stroke-width="4"/>
    <text class="label-text" x="377" y="450" font-size="34" text-anchor="middle">CLOTHES WASHER</text>
  </g>
  <g class="product-label label-fridge">
    <rect x="2" y="566" width="270" height="54" fill="var(--red)" stroke="var(--white)" stroke-width="4"/>
    <text class="label-text" x="137" y="606" font-size="40" text-anchor="middle">FRIDGEFREEZER</text>
  </g>
  <g class="product-label label-dishwasher">
    <rect x="290" y="740" width="208" height="60" fill="var(--green-deep)" stroke="var(--white)" stroke-width="4"/>
    <text class="label-text" x="394" y="784" font-size="44" text-anchor="middle">DISHWASHER</text>
  </g>

  <!-- warranty panel -->
  <g class="warranty-panel">
    <path d="M0 752 L212 735 L200 938 L0 938 Z" fill="var(--yellow)"/>
    <text class="warranty-text" x="12" y="895" font-size="140">5</text>
    <text class="warranty-text" x="72" y="846" font-size="60">YEARS</text>
    <text class="warranty-text" x="72" y="880" font-size="32">WARRANTY</text>
  </g>
</svg>
</body>
</html>
```